Heronbay Poolworks, LLC Business Card

We have a well designed logo that we need incorporated into a professional and unique business card. Heronbay Poolworks provides professional swimming pool management. From openings to closings, inspections, chemicals, maintenance, lifeguard, safety audits, learn to swim lessons, etc. etc.
Different colors of blue are ideal. The final design should include water, clean water (very clean crystal clear water), and perhaps safety.
content/design ideas:
Milo Fenster, President - Owner
milo@heronbaypoolworks.example
office: 555-412-8391
cell: 555-630-2175
www.heronbaypoolworks.example
"Your Pool: Safer, Cleaner, Clearer"
Target Market(s)
Our customers are mostly home owners associations and property management companies. Adults, aged 25 to 55. Mostly with young children.
Industry/Entity Type
Safety
Look and feel

```html
<!DOCTYPE html>
<html lang="en">
<head>
<meta charset="utf-8">
<title>Heronbay Poolworks, LLC — Business Card</title>
<link rel="stylesheet" href="https://fonts.googleapis.com/css2?family=Arimo:wght@400;700&display=swap">
<style>
  :root {
    --backdrop: #2b2b2d;
    --card-white: #f3f3f3;
    --pool-light: #7fdcf7;
    --pool-mid: #35b6ec;
    --pool-deep: #1690d8;
    --ring-blue: #1f7fe0;
    --brand-blue: #2f6aa8;
    --ink: #2a2a2a;
    --ink-soft: #4a4a4a;
    --rule: #7f93ab;
    --white: #ffffff;
  }
  * { margin: 0; padding: 0; box-sizing: border-box; }
  html, body {
    width: 1200px; height: 900px; overflow: hidden;
    background: var(--backdrop);
    font-family: "Arimo", Arial, sans-serif;
  }
  .stage { position: relative; width: 1200px; height: 900px; }

  .card {
    position: absolute; left: 354px; width: 488px; height: 271px;
    overflow: hidden;
  }
  .card-front { top: 157px; }
  .card-back { top: 467px; background: var(--card-white); }

  .pool-photo {
    position: absolute; inset: 0;
    background:
      radial-gradient(ellipse 110px 70px at 72% 62%, rgba(31,127,224,0.85) 0%, transparent 100%),
      radial-gradient(ellipse 160px 110px at 35% 45%, rgba(127,220,247,0.55) 0%, transparent 100%),
      radial-gradient(ellipse 140px 90px at 85% 20%, rgba(127,220,247,0.5) 0%, transparent 100%),
      linear-gradient(160deg, var(--pool-light) 0%, var(--pool-mid) 45%, var(--pool-deep) 100%);
  }
  .tagline {
    position: absolute; left: 26px; top: 25px;
    color: var(--white); font-size: 19px; line-height: 24px; font-weight: 400;
  }

  .brand-mark {
    position: absolute; left: 38px; top: 28px;
    width: 62px; height: 62px; border-radius: 50%;
    background: var(--brand-blue);
  }
  .brand-name {
    position: absolute; left: 56px; top: 101px;
    font-size: 25px; font-weight: 700; color: var(--brand-blue);
    letter-spacing: -0.3px; white-space: nowrap;
  }

  .holder { position: absolute; left: 60px; top: 162px; }
  .holder-name { font-size: 18px; color: var(--ink); letter-spacing: 0.3px; }
  .holder-title { font-size: 13px; color: var(--ink-soft); margin-top: 4px; }

  .contacts { position: absolute; left: 244px; top: 163px; font-size: 12px; color: var(--ink); line-height: 17px; white-space: nowrap; }
  .contacts .label { color: var(--brand-blue); display: inline-block; width: 15px; font-size: 13px; }
  .contacts .rule { border: 0; border-top: 1px solid var(--rule); width: 214px; margin: 9px 0 6px; }
  .contacts .web { color: var(--brand-blue); font-size: 12.5px; }
</style>
</head>
<body>
<main class="stage">
  <section class="card card-front">
    <div class="pool-photo" role="img" aria-label="Photo of a woman in a sun hat relaxing on a blue inflatable ring in crystal clear pool water"></div>
    <p class="tagline">YOUR POOL:<br>Safer, Cleaner, Clearer</p>
  </section>

  <section class="card card-back">
    <span class="brand-mark"></span>
    <p class="brand-name">Heronbay Poolworks</p>
    <div class="holder">
      <p class="holder-name">MILO FENSTER</p>
      <p class="holder-title">President - Owner</p>
    </div>
    <div class="contacts">
      <p><span class="label">T</span>555-412-8391</p>
      <p><span class="label">M</span>555-630-2175</p>
      <p><span class="label">E</span>milo@heronbaypoolworks.example</p>
      <hr class="rule">
      <p class="web">www.heronbaypoolworks.example</p>
    </div>
  </section>
</main>
</body>
</html>
```